R.T. Framers Postcard Design

We need a postcard designed around the utility rebates for window installations. For customers who have Electric heated homes can receive $6 per square foot for each window and patio door and for Natural gas heated homes, they can get $75.00 per window and patio door. The $6 per square foot for electric heated customers is the better rebate averaging about $1000.00 for a house with 10 windows and a patio door. Our Company colors are maroon, black and white, we would like to have a post card designed around these colors. The postcard should be designed to share about these 2 rebates and having a window installation theme. You can use pictures off of our website...www.rtframers-example.com

Target Market(s)

Homeowners with electric heat or Natural gas heat

Industry/Entity Type

Utility

Requirements
Must have
• Blank white square on the back for me to hand write address information.

```html
<!DOCTYPE html>
<html lang="en">
<head>
<meta charset="utf-8">
<title>RT Framers Rebate Postcard</title>
<link rel="stylesheet" href="https://fonts.googleapis.com/css2?family=Roboto:ital,wght@0,400;0,500;0,700;0,900;1,400;1,700&display=swap">
<style>
  :root {
    --maroon: #8e1230;
    --maroon-dark: #6f0c24;
    --black: #06070b;
    --white: #ffffff;
    --ink: #1c1c1c;
    --stage-dark: #0b0b0b;
    --stage-mid: #3a3a3a;
    --paper: #f6f5f3;
  }
  * { box-sizing: border-box; margin: 0; padding: 0; }
  html, body { width: 815px; height: 1200px; overflow: hidden; }
  body {
    font-family: "Roboto", Arial, sans-serif;
    background: radial-gradient(ellipse at 50% 45%, var(--stage-mid) 0%, #1c1c1c 55%, var(--stage-dark) 100%);
    position: relative;
    color: var(--ink);
  }
  .card { position: absolute; left: 68px; width: 679px; overflow: hidden; box-shadow: 0 6px 18px rgba(0,0,0,.5); }

  /* ---------- Front ---------- */
  .front { top: 65px; height: 525px; background: var(--white); }
  .hero-photo {
    position: absolute; inset: 0 0 250px 0;
    background: linear-gradient(100deg, #c9d4c0 0%, #eef0ec 25%, #f5f3ef 45%, #e9e4dc 65%, #d8c8a8 100%);
  }
  .brand-tab {
    position: absolute; left: 2px; top: 35px; width: 235px; height: 45px;
    background: var(--white); display: flex; align-items: center; padding-left: 28px; gap: 10px;
    clip-path: polygon(0 0, 100% 0, 94% 100%, 0 100%);
  }
  .brand-tab .mark { width: 22px; height: 22px; background: var(--maroon); }
  .brand-tab .name { font-size: 21px; font-weight: 700; color: var(--ink); }

  .offer-band {
    position: absolute; left: 0; top: 275px; width: 100%; height: 203px; background: var(--maroon);
  }
  .headline { position: absolute; left: 42px; top: 8px; display: flex; align-items: flex-end; }
  .headline .get {
    background: var(--black); color: var(--white); font-weight: 900; font-size: 24px;
    padding: 1px 6px 1px 16px; margin-bottom: 9px; letter-spacing: .5px;
    clip-path: polygon(10px 0, 100% 0, 100% 100%, 10px 100%, 0 50%);
  }
  .headline .rebates { color: var(--white); font-weight: 900; font-size: 54px; line-height: 1; letter-spacing: .5px; }
  .subhead { position: absolute; left: 58px; top: 62px; color: var(--white); font-weight: 700; font-size: 19.5px; letter-spacing: .3px; }
  .rebate { position: absolute; top: 90px; color: var(--white); }
  .rebate.gas { left: 39px; }
  .rebate.electric { left: 248px; }
  .rebate .label { font-size: 14px; font-weight: 700; }
  .rebate .amount { font-size: 40px; font-weight: 700; line-height: 1.05; display: flex; align-items: center; gap: 4px; }
  .rebate .unit { font-size: 16px; font-weight: 400; line-height: .95; }
  .rebate .note { font-size: 12px; font-weight: 400; opacity: .9; margin-top: 2px; }
  .divider { position: absolute; left: 233px; top: 88px; width: 1px; height: 82px; background: rgba(255,255,255,.8); }
  .tagline { position: absolute; left: 72px; top: 178px; color: var(--white); font-size: 14px; font-weight: 700; font-style: italic; }

  .inset-frame {
    position: absolute; left: 443px; top: 224px; width: 202px; height: 256px; background: var(--white);
    padding: 10px 11px 0 11px; box-shadow: 0 2px 6px rgba(0,0,0,.3);
  }
  .inset-photo { width: 100%; height: 117px; }
  .inset-photo.living { background: linear-gradient(180deg, #c9b97a 0%, #a99a60 45%, #6a5a3a 100%); }
  .inset-photo.family { margin-top: 0; height: 118px; background: linear-gradient(180deg, #8a4a2c 0%, #c29c74 50%, #7a5a3c 100%); }

  .contact-bar {
    position: absolute; left: 0; bottom: 0; width: 100%; height: 47px; background: var(--black);
    color: var(--white); font-size: 17.5px; font-weight: 500; display: flex; align-items: center; justify-content: center; gap: 6px;
  }

  /* ---------- Back ---------- */
  .back { top: 608px; height: 527px; background: var(--paper); }
  .back-photo {
    position: absolute; inset: 0;
    background: linear-gradient(90deg, rgba(200,205,195,.55) 0%, rgba(230,232,226,.5) 35%, rgba(246,245,243,0) 62%);
  }
  .testimonial { position: absolute; left: 50px; top: 45px; }
  .quote-mark { position: absolute; width: 36px; height: 30px; }
  .quote-mark.open { left: 106px; top: 0; }
  .quote-mark.close { left: 106px; top: 138px; }
  .testimonial blockquote { position: absolute; left: 0; top: 45px; width: 300px; font-style: italic; font-size: 15.5px; line-height: 1.3; color: var(--ink); }
  .testimonial cite { display: block; font-weight: 700; font-style: italic; }

  .company { position: absolute; left: 50px; top: 222px; }
  .company .mark { width: 80px; height: 58px; background: var(--maroon); }
  .company .name { margin-top: 7px; font-size: 31px; font-weight: 700; color: var(--ink); }
  .company address { font-style: normal; font-size: 16px; line-height: 1.3; margin-top: 6px; }
  .contact-list { list-style: none; margin-top: 6px; }
  .contact-list li { display: flex; align-items: center; gap: 6px; font-size: 18px; line-height: 1.3; }
  .contact-list li.strong { font-weight: 700; }
  .contact-list svg { width: 13px; height: 13px; flex: none; }

  .address-area { position: absolute; left: 380px; top: 30px; width: 270px; height: 467px; background: var(--white); opacity: .7; }
</style>
</head>
<body>

<section class="card front" aria-label="Postcard front">
  <div class="hero-photo" role="img" aria-label="Photo of a woman holding a mug beside bright new white-framed windows"></div>

  <div class="brand-tab">
    <span class="mark"></span>
    <span class="name">RT FRAMERS</span>
  </div>

  <div class="offer-band">
    <h1 class="headline"><span class="get">GET</span><span class="rebates">REBATES</span></h1>
    <p class="subhead">FOR WINDOW INSTALLATIONS</p>

    <div class="rebate gas">
      <p class="label">Natural gas heated homes</p>
      <p class="amount">$75.00</p>
      <p class="note">per window and patio door</p>
    </div>
    <div class="divider"></div>
    <div class="rebate electric">
      <p class="label">Electric heated homes</p>
      <p class="amount">$6 <span class="unit">PER<br>SQ.FT.</span></p>
      <p class="note">each window and patio door</p>
    </div>

    <p class="tagline">Installing windows the right way since 1985</p>
  </div>

  <div class="inset-frame">
    <div class="inset-photo living" role="img" aria-label="Living room with a leather sofa in front of a large window"></div>
    <div class="inset-photo family" role="img" aria-label="Warm family room with a wide picture window"></div>
  </div>

  <div class="contact-bar">
    <span>www.rtframers-example.com</span><span>|</span><strong>425-555-0142</strong><span>|</span><span>dana@rtframers-example.com</span>
  </div>
</section>

<section class="card back" aria-label="Postcard back">
  <div class="back-photo" role="img" aria-label="Faded view of a sunlit window interior"></div>
  <div class="address-area" aria-label="Space for handwritten address"></div>

  <div class="testimonial">
    <svg class="quote-mark open" viewBox="0 0 36 30" aria-hidden="true">
      <path fill="var(--maroon)" d="M16 0v6c-5 1-7 4-7 8h7v16H0V15C0 6 5 1 16 0zm20 0v6c-5 1-7 4-7 8h7v16H20V15C20 6 25 1 36 0z"/>
    </svg>
    <blockquote>
      SPLENDID JOB! Thanks again.<br>
      I will be recommending your<br>
      services to my friends and family.
      <cite>- Martin Hale<br>&nbsp;&nbsp;Everett, WA</cite>
    </blockquote>
    <svg class="quote-mark close" viewBox="0 0 36 30" aria-hidden="true">
      <path fill="var(--maroon)" d="M20 30v-6c5-1 7-4 7-8h-7V0h16v15c0 9-5 14-16 15zM0 30v-6c5-1 7-4 7-8H0V0h16v15C16 24 11 29 0 30z"/>
    </svg>
  </div>

  <div class="company">
    <div class="mark"></div>
    <p class="name">RT FRAMERS</p>
    <address>2150 Cedar Ridge Road NE<br>Lakewood, Washington<br>98499, United States</address>
    <ul class="contact-list">
      <li><svg viewBox="0 0 13 13" aria-hidden="true"><circle cx="6.5" cy="6.5" r="6.5" fill="var(--maroon)"/><circle cx="6.5" cy="6.5" r="3.5" fill="none" stroke="#fff" stroke-width="1.2"/></svg>www.rtframers-example.com</li>
      <li class="strong"><svg viewBox="0 0 13 13" aria-hidden="true"><rect width="13" height="13" rx="2" fill="var(--maroon)"/><path d="M4 3l1.6 2-1 1c.6 1.2 1.3 1.9 2.5 2.5l1-1L10 9l-.8 1.3C6 10 3 7 2.8 3.8z" fill="#fff"/></svg>425-555-0142</li>
      <li class="strong"><svg viewBox="0 0 13 13" aria-hidden="true"><rect width="13" height="13" rx="2" fill="var(--maroon)"/><rect x="3" y="6" width="7" height="4" fill="#fff"/><path d="M2.5 5.5c2-2 6-2 8 0" stroke="#fff" stroke-width="1.3" fill="none"/></svg>360-555-0187</li>
      <li><svg viewBox="0 0 13 13" aria-hidden="true"><rect width="13" height="13" rx="2" fill="var(--maroon)"/><rect x="2.5" y="3.5" width="8" height="6" fill="#fff"/><path d="M2.5 3.5l4 3.3 4-3.3" stroke="var(--maroon)" stroke-width="1" fill="none"/></svg>dana@rtframers-example.com</li>
    </ul>
  </div>
</section>

</body>
</html>
```